3 JPG Website Page Mockups need tidying / made into layered PSDs

Our website is aimed at creating a financial eduction site for females.

We have mockups of each page which are provided in jpeg.... but they need to be tidied up, layered into PSD (with descriptive layer names to allow coding from and no flattening - each object needs it's own layer) and we welcome any creative improvements suggested (although we are pretty happy with the way it's laid out at the moment as it is), without changing the feel, colour scheme or functionality of the site.

Three pages are needed:
Home page when not logged in
Home page when logged in
Topic header page

Please just upload the homepage to bid for the job... the winning designer will then have 5 days after they've been chosen to supply the psds of the other 2 pages .

I have also uploaded an image that can be used as a placeholder in the top box.
Thanks

As requested... Current font is Gill Sans MT

Thanks

Hi
Thanks for your designs.... For those of you still using the 4 circles (which I quite like), but haven't yet done so, could you see if you can move them around slightly to that the words don't get covered by the next circle?

Thanks

Reason: Designe has asked for An extension to work on new icons... would like to give them the time to see what they come up with, thanks

Industry/Entity Type

Financial

Requirements
Must have
• Maintain current feel & colour scheme of the website

```html
<!DOCTYPE html>
<html lang="en">
<head>
<meta charset="utf-8">
<title>Her Money Hub – Home</title>
<link rel="stylesheet" href="https://fonts.googleapis.com/css2?family=Bebas+Neue&family=Lato:wght@400;700&display=swap">
<style>
:root{
  --teal:#0d949c;
  --teal-dark:#0a7980;
  --teal-bright:#1db7c3;
  --teal-light:#b8f1f6;
  --orange:#e0492a;
  --orange-btn:#e4461e;
  --ink:#333;
  --grey-band:#e3e3e3;
  --hero-band:#efefef;
  --tab-grey:#8e8e8e;
  --sage:#a6bf95;
  --sage-dark:#7fa36c;
  --cream:#f2e8c2;
  --poll-blue:#dde8f3;
  --icon-teal:#4fcbd6;
  --caption-green:rgba(98,150,112,.92);
}
*{box-sizing:border-box;margin:0;padding:0}
html,body{width:1200px;height:1043px;overflow:hidden}
body{position:relative;font-family:"Lato",sans-serif;color:var(--ink);background:#fff}
.abs{position:absolute}

/* main navigation */
.main-nav{left:0;top:0;width:1200px;height:54px;background:linear-gradient(#12a6ad,var(--teal-dark));box-shadow:0 2px 3px rgba(0,0,0,.25);z-index:2}
.main-nav a{position:absolute;top:0;line-height:54px;color:#fff;font-size:15.5px;text-decoration:none;transform:translateX(-50%);white-space:nowrap}
.main-nav .is-current{top:8px;left:73px;width:96px;height:36px;line-height:36px;text-align:center;border-radius:4px;background:linear-gradient(#e8feff,var(--teal-light));color:#14464a;box-shadow:0 0 3px rgba(255,255,255,.8)}

/* header */
.site-header{left:0;top:54px;width:1200px;height:198px;background:var(--grey-band)}
.brand{left:28px;top:62px;font-size:48px;color:var(--ink);font-weight:400}
.search-title{left:418px;top:26px;font-family:"Bebas Neue",sans-serif;font-size:27px;color:var(--orange);letter-spacing:.3px}
.search-box{left:418px;top:74px;width:378px;height:45px;border-radius:23px;background:#fff;border:1px solid #c9c9c9;box-shadow:inset 0 1px 3px rgba(0,0,0,.15)}
.search-box span{position:absolute;left:20px;top:12px;font-size:16.5px;color:#8b8b8b}
.search-box svg{position:absolute;right:14px;top:9px}
.pill-btn{top:74px;width:170px;height:45px;border-radius:23px;color:#fff;font-size:16px;padding:12px 0 0 20px;box-shadow:0 1px 2px rgba(0,0,0,.25)}
.pill-btn svg{position:absolute;right:12px;top:11px}
.btn-adviser{left:814px;background:var(--teal-bright);color:#0f3d44}
.btn-contact{left:996px;background:var(--orange-btn)}
.quick-links{left:419px;top:146px;height:27px;font-size:17.5px;color:#222}
.quick-links span{position:absolute;top:3px;white-space:nowrap}
.quick-links .tab-active{left:0;top:0;width:159px;height:27px;line-height:25px;text-align:center;background:var(--tab-grey);color:#fff;border-radius:3px;border:1px solid #777}

/* hero */
.hero{left:0;top:252px;width:1200px;height:284px;background:var(--hero-band);border-bottom:2px solid var(--teal)}
.video-frame{left:25px;top:17px;width:299px;height:247px;background:#fff;border:1px solid #bcbcbc;border-radius:4px;box-shadow:0 1px 3px rgba(0,0,0,.2)}
.video-still{position:absolute;left:9px;top:8px;width:282px;height:210px;background:linear-gradient(135deg,#5a3b2e,#8a5a44 45%,#3a2a24)}
.video-play{position:absolute;left:124px;top:90px;width:52px;height:46px;background:rgba(0,0,0,.45)}
.video-caption{position:absolute;left:12px;top:162px;width:170px;height:46px;background:var(--caption-green);color:#fff;padding:5px 0 0 14px;white-space:nowrap;overflow:hidden}
.video-caption b{display:block;font-weight:400;font-size:13px;line-height:15px;letter-spacing:2px;text-transform:uppercase}
.video-caption i{display:block;font-style:normal;font-size:8px;line-height:10px;letter-spacing:.6px;text-transform:uppercase}
.video-controls{position:absolute;left:9px;top:223px;width:282px;height:14px}
.topic-label{left:347px;top:36px;font-family:"Bebas Neue",sans-serif;font-size:31px;color:#2f2f2f}
.topic-headline{left:347px;top:76px;font-family:"Bebas Neue",sans-serif;font-size:43px;line-height:50px;color:var(--orange);letter-spacing:.3px}
.learn-more{left:347px;top:185px;font-size:19px;color:#333}
.bubble{border-radius:50%;text-align:center;display:flex;flex-direction:column;align-items:center;justify-content:center}
.bubble-guide{left:738px;top:126px;width:84px;height:84px;background:#fff;border:5px solid #b5c8aa;font-size:11px;font-weight:700;color:#222;line-height:13px}
.bubble-guide strong{font-size:16px;line-height:18px}
.bubble-guide em{font-style:normal;color:var(--sage-dark);font-size:10px}
.bubble-poll{left:811px;top:67px;width:130px;height:130px;background:var(--poll-blue);border:2px solid #c4d6e6;font-size:13px;font-weight:700;color:#222;padding-top:32px}
.bubble-poll em{font-style:normal;font-weight:400;color:#4f8ec4;font-size:14px}
.bubble-story{left:926px;top:26px;width:116px;height:116px;background:#fff;border:6px solid var(--cream);font-size:13px;font-weight:700;color:#222;line-height:21px}
.bubble-story em{font-style:normal;color:var(--sage-dark);font-size:12px}
.bubble-ask{left:1017px;top:65px;width:158px;height:158px;background:var(--sage);border:3px solid #d9e4d0;color:#fff;font-size:12.5px;line-height:16px;padding:0 18px}
.bubble-ask em{font-style:normal;font-size:10.5px;margin-top:8px}

/* content */
.content{left:0;top:536px;width:1200px;height:386px;background:linear-gradient(#cddbdc,#e9f0f1 70%,#eef3f4)}
.section-title{font-family:"Bebas Neue",sans-serif;font-weight:400;font-size:36px;color:var(--orange);letter-spacing:.2px;line-height:36px}
.newsletter{left:34px;top:18px;width:559px}
.newsletter p{font-size:15.5px;line-height:20px;text-align:justify;color:#333;margin-top:20px}
.newsletter .section-title+p{margin-top:22px}
.newsletter .see-more{position:absolute;top:290px;left:0;margin:0;font-weight:700;color:#444;font-size:15.5px;text-align:left}
.divider{left:624px;top:18px;width:1px;height:350px;background:#a9b3b4}
.articles{left:654px;top:18px;width:520px}
.article{position:absolute;left:0;height:42px;display:flex;align-items:center;font-size:21.5px;color:#444;line-height:24px;white-space:nowrap}
.article svg{flex:none;margin-right:18px}

/* footer */
.life-stages{left:0;top:922px;width:1200px;height:121px;background:linear-gradient(#cfcfcf,#e9e9e9 40%,#efefef);border-top:2px solid #b6b6b6}
.stage{position:absolute;top:18px;width:140px;margin-left:-70px;text-align:center;font-family:Arial,Helvetica,sans-serif;font-weight:700;font-size:15.5px;color:#222}
.stage svg{display:block;margin:0 auto 6px}
</style>
</head>
<body>

<nav class="main-nav abs">
  <a class="is-current" href="#">Home</a>
  <a href="#" style="left:196px">Polls Events</a>
  <a href="#" style="left:349px">Learning Centre</a>
  <a href="#" style="left:516px">Find an Adviser</a>
  <a href="#" style="left:674px">Ask a Qestion</a>
  <a href="#" style="left:814px">About Us</a>
</nav>

<header class="site-header abs">
  <div class="brand abs">Company Logo</div>
  <div class="search-title abs">What are you looking for?</div>
  <div class="search-box abs">
    <span>Search Her Money Hub for...</span>
    <svg width="28" height="28" viewBox="0 0 28 28"><circle cx="11" cy="11" r="8" fill="none" stroke="#1aa8b4" stroke-width="3.5"/><line x1="17" y1="17" x2="25" y2="25" stroke="#1aa8b4" stroke-width="5" stroke-linecap="round"/></svg>
  </div>
  <div class="pill-btn btn-adviser abs">Find an Adviser
    <svg width="23" height="23" viewBox="0 0 23 23"><circle cx="11.5" cy="11.5" r="11" fill="#fff"/><path d="M6.5 9h10l-5 6z" fill="var(--teal-bright)"/></svg>
  </div>
  <div class="pill-btn btn-contact abs">Contact Us
    <svg width="23" height="23" viewBox="0 0 23 23"><circle cx="11.5" cy="11.5" r="11" fill="#fff"/><path d="M6.5 9h10l-5 6z" fill="var(--orange-btn)"/></svg>
  </div>
  <div class="quick-links abs">
    <span class="tab-active">Popular Searches</span>
    <span style="left:177px">Explore the Learning Centre</span>
    <span style="left:420px">Ask a Question</span>
  </div>
</header>

<section class="hero abs">
  <div class="video-frame abs">
    <div class="video-still" role="img" aria-label="Video still of the featured speaker in an office setting"></div>
    <div class="video-play">
      <svg width="52" height="46" viewBox="0 0 52 46"><path d="M20 13l16 10-16 10z" fill="#fff"/></svg>
    </div>
    <div class="video-caption">
      <b>Dana Whitford</b>
      <i>Founder, Chairman &amp; CEO</i>
      <i>Harbour &amp; Co.</i>
    </div>
    <svg class="video-controls" viewBox="0 0 282 14">
      <path d="M2 4l5 3-5 3z M11 4h5v6h-5z" fill="#6a8f6f"/>
      <text x="24" y="10" font-size="8" fill="#6a8f6f" font-family="Arial">00:00</text>
      <rect x="52" y="6" width="140" height="2" fill="#c9c9c9"/>
      <text x="196" y="10" font-size="8" fill="#6a8f6f" font-family="Arial">00:00</text>
      <rect x="230" y="4" width="6" height="6" fill="none" stroke="#6a8f6f"/>
      <rect x="244" y="6" width="30" height="2" fill="#c9c9c9"/>
    </svg>
  </div>

  <div class="topic-label abs">July Topic: Preparing for Retirement</div>
  <div class="topic-headline abs">Tomorrow can belong to those<br>who prepare today</div>
  <div class="learn-more abs">Learn More ›</div>

  <div class="bubble bubble-poll abs">
    <svg width="100" height="36" viewBox="0 0 100 36">
      <g fill="#8fb07f">
        <rect x="2" y="28" width="6" height="6"/><rect x="10" y="26" width="6" height="8"/><rect x="18" y="24" width="6" height="10"/><rect x="26" y="20" width="6" height="14"/><rect x="34" y="22" width="6" height="12"/><rect x="42" y="16" width="6" height="18"/><rect x="50" y="14" width="6" height="20"/><rect x="58" y="10" width="6" height="24"/><rect x="66" y="12" width="6" height="22"/><rect x="74" y="6" width="6" height="28"/><rect x="82" y="4" width="6" height="30"/><rect x="90" y="8" width="6" height="26"/>
      </g>
    </svg>
    <span style="margin-top:6px">Take Our Poll</span>
    <em>Vote ›</em>
  </div>
  <div class="bubble bubble-guide abs">5 Minute<strong>Guide</strong><em>PDF ›</em></div>
  <div class="bubble bubble-story abs">Real Women<br>Real Stories<em>See Video</em></div>
  <div class="bubble bubble-ask abs">Have questions about Life Stages &amp; Planning? Ask a question or see what others have asked...<em>More ›</em></div>
</section>

<main class="content abs">
  <div class="newsletter abs">
    <h2 class="section-title">Catch up with our latest newsletter</h2>
    <p>Lorem ipsum dolor sit amet, consectetur adipiscing elit. Nunc vitae felis vel nunc laoreet congue. Vivamus adipiscing quam sed sapien bibendum vel varius massa venenatis.</p>
    <p>Phasellus elit metus, sollicitudin ut mattis et, sollicitudin vitae enim. Vestibulum ante ipsum primis in faucibus orci luctus et ultrices posuere cubilia Curae; Ut ac sem augue. In sapien nisi, dapibus a blandit sagittis, vestibulum vel nulla. In bibendum augue urna, non consectetur lectus.</p>
    <p>Proin a tortor id dolor malesuada ornare. Mauris eu risus sapien.</p>
    <p class="see-more">See the Newsletter Now ›</p>
  </div>
  <div class="divider abs"></div>
  <div class="articles abs">
    <h2 class="section-title">Latest Article Interest</h2>
    <div class="article" style="top:57px">
      <svg width="40" height="40" viewBox="0 0 40 40"><circle cx="20" cy="20" r="18.5" fill="#fff" stroke="#b9c3c4"/><path d="M11 27v-7l5-5 4 4 4-4 5 5v7z" fill="#e75a2b"/></svg>
      What is the real cost of having a baby</div>
    <div class="article" style="top:133px">
      <svg width="40" height="40" viewBox="0 0 40 40"><circle cx="20" cy="20" r="18.5" fill="#fff" stroke="#b9c3c4"/><path d="M12 12v16h17" fill="none" stroke="#555" stroke-width="1.5"/><path d="M14 26v-4h2v4zM18 26v-6h2v6zM22 26v-8h2v8zM26 26v-5h2v5z" fill="#c0392b"/><path d="M13 21l5-4 4 2 6-6" fill="none" stroke="#c0392b" stroke-width="1.5"/></svg>
      Understanding the risk and return of<br>different assets type</div>
    <div class="article" style="top:212px">
      <svg width="40" height="40" viewBox="0 0 40 40"><circle cx="20" cy="20" r="18.5" fill="#fff" stroke="#b9c3c4"/><rect x="11" y="11" width="16" height="17" fill="#fff" stroke="#555" stroke-width="1.5"/><rect x="11" y="11" width="16" height="4" fill="#c0392b"/><text x="14" y="25" font-size="9" font-family="Arial" font-weight="700" fill="#333">31</text><circle cx="26" cy="26" r="4.5" fill="#fff" stroke="#555"/></svg>
      How much do I need to retire ?</div>
    <div class="article" style="top:282px">
      <svg width="40" height="40" viewBox="0 0 40 40"><circle cx="20" cy="20" r="18.5" fill="#fff" stroke="#b9c3c4"/><path d="M12 12v16h17" fill="none" stroke="#555" stroke-width="1.5"/><path d="M14 26v-4h2v4zM18 26v-6h2v6zM22 26v-8h2v8zM26 26v-5h2v5z" fill="#c0392b"/><path d="M13 21l5-4 4 2 6-6" fill="none" stroke="#c0392b" stroke-width="1.5"/></svg>
      Interest rates and you</div>
  </div>
</main>

<nav class="life-stages abs" aria-label="Life stages">
  <div class="stage" style="left:100px">
    <svg width="56" height="56" viewBox="0 0 56 56"><circle cx="28" cy="28" r="26.5" fill="#fff" stroke="#555" stroke-width="2"/><circle cx="28" cy="20" r="7" fill="#8a8f96"/><path d="M16 44c0-10 5-15 12-15s12 5 12 15z" fill="#8a8f96"/></svg>Welcome</div>
  <div class="stage" style="left:241px">
    <svg width="56" height="56" viewBox="0 0 56 56"><circle cx="28" cy="28" r="26.5" fill="var(--icon-teal)" stroke="#333" stroke-width="2"/><rect x="17" y="16" width="22" height="22" rx="2" fill="#a0244d"/><g fill="#fff"><circle cx="22" cy="30" r="2"/><circle cx="28" cy="30" r="2"/><circle cx="34" cy="30" r="2"/></g></svg>Events</div>
  <div class="stage" style="left:382px">
    <svg width="56" height="56" viewBox="0 0 56 56"><circle cx="28" cy="28" r="26.5" fill="var(--icon-teal)" stroke="#333" stroke-width="2"/><rect x="14" y="16" width="28" height="19" rx="2" fill="#1e2a33"/><path d="M25 21l8 4.5-8 4.5z" fill="var(--icon-teal)"/><rect x="20" y="38" width="16" height="3" fill="#1e2a33"/></svg>Webcasts</div>
  <div class="stage" style="left:528px">
    <svg width="56" height="56" viewBox="0 0 56 56"><circle cx="28" cy="28" r="26.5" fill="var(--icon-teal)" stroke="#333" stroke-width="2"/><path d="M15 40V28l7-8 6 6 6-6 7 8v12z" fill="#e75a2b"/><path d="M28 12l5 5-5 5-5-5z" fill="#e75a2b"/></svg>My Family</div>
  <div class="stage" style="left:668px">
    <svg width="56" height="56" viewBox="0 0 56 56"><circle cx="28" cy="28" r="26.5" fill="var(--icon-teal)" stroke="#333" stroke-width="2"/><path d="M16 15v25h25" fill="none" stroke="#333" stroke-width="2"/><path d="M19 38v-6h3v6zM24 38v-9h3v9zM29 38v-12h3v12zM34 38v-8h3v8z" fill="#c0392b"/><path d="M18 30l7-7 5 3 8-9" fill="none" stroke="#c0392b" stroke-width="2"/></svg>My Investments</div>
  <div class="stage" style="left:816px">
    <svg width="56" height="56" viewBox="0 0 56 56"><circle cx="28" cy="28" r="26.5" fill="var(--icon-teal)" stroke="#333" stroke-width="2"/><rect x="15" y="14" width="23" height="25" fill="#fff" stroke="#333" stroke-width="1.5"/><rect x="15" y="14" width="23" height="6" fill="#c0392b"/><text x="19" y="34" font-size="12" font-family="Arial" font-weight="700" fill="#333">31</text><circle cx="38" cy="37" r="6" fill="#fff" stroke="#333" stroke-width="1.5"/></svg>My Retirement</div>
  <div class="stage" style="left:949px">
    <svg width="56" height="56" viewBox="0 0 56 56"><circle cx="28" cy="28" r="26.5" fill="var(--icon-teal)" stroke="#333" stroke-width="2"/><path d="M18 18l14-6 8 14-14 8z" fill="#c0392b"/><path d="M14 34l10-6 6 8-10 6z" fill="#fff" stroke="#777"/></svg>My Estate</div>
  <div class="stage" style="left:1100px">
    <svg width="56" height="56" viewBox="0 0 56 56"><circle cx="28" cy="28" r="26.5" fill="var(--icon-teal)" stroke="#333" stroke-width="2"/><circle cx="28" cy="28" r="17" fill="#ea6a1f"/><circle cx="28" cy="28" r="12" fill="none" stroke="#fff" stroke-width="2"/><circle cx="28" cy="22" r="3" fill="#fff"/><path d="M20 34c3-5 13-5 16 0z" fill="#fff"/></svg>My Lifestyle</div>
</nav>

</body>
</html>
```